Business cards for Champion Suri Alpaca Breeder

I am a seed stock Suri Alpaca breeder. I am looking for a business card design that is tactile with my logo or part of my logo embossed or debossed. I am open to other ideas.
My logo is available in detailed and simplified version. To get a feel for my style visit my website velmorfieldfleece.com

Target Market(s)

Alpaca breeders

Industry/Entity Type

Alpaca / Livestock

Contact Information for Business Card

Logo, Dora Plume, VELMORandFIELD.com, Saint Louis, MO 314-555-0172

Colors
0054AA
0677BA
7BADD7
CADEEF
E8F1F8

Requirements
Must have
• use brand guide
Nice to have
• embossed or debossed, incorporating a simple plaid use complimentary colors in logo
Should not have
• cartoon alpacas

```html
<!DOCTYPE html>
<html lang="en">
<head>
<meta charset="utf-8">
<title>Velmor &amp; Field — Business Cards</title>
<link rel="stylesheet" href="https://fonts.googleapis.com/css2?family=Cinzel:wght@400&family=Montserrat:wght@400;500&display=swap">
<style>
  :root {
    --stage: #3a332e;
    --card-white: #ffffff;
    --card-sand-light: #faf7f1;
    --card-sand: #ddd0bb;
    --ink: #2a2522;
    --ink-soft: #4a4440;
    --accent: #c8b69c;
    --rule: #d8cbb8;
  }
  * { box-sizing: border-box; margin: 0; padding: 0; }
  html, body { width: 1200px; height: 786px; overflow: hidden; }
  body {
    background: var(--stage);
    display: flex;
    align-items: center;
    justify-content: center;
    gap: 56px;
  }
  .card {
    width: 520px;
    height: 297px;
    position: relative;
    box-shadow: 0 10px 24px rgba(0,0,0,.35);
  }
  .card--front { background: var(--card-white); }
  .card--back {
    background: radial-gradient(ellipse at 50% 38%, var(--card-sand-light) 0%, #ece3d5 45%, var(--card-sand) 100%);
    display: flex;
    align-items: center;
    justify-content: center;
  }
  .brand {
    display: flex;
    flex-direction: column;
    align-items: center;
    gap: 18px;
  }
  .brand__dot {
    width: 62px;
    height: 62px;
    border-radius: 50%;
    background: var(--accent);
  }
  .brand__name {
    font-family: "Cinzel", serif;
    font-weight: 400;
    color: var(--ink);
    letter-spacing: .04em;
    white-space: nowrap;
  }
  .card--front .brand {
    position: absolute;
    left: 40px;
    width: 200px;
    top: 78px;
  }
  .card--front .brand__name { font-size: 19px; }
  .card--back .brand__dot { width: 86px; height: 86px; }
  .card--back .brand__name { font-size: 28px; }
  .divider {
    position: absolute;
    left: 262px;
    top: 64px;
    width: 1px;
    height: 170px;
    background: var(--rule);
  }
  .contact {
    position: absolute;
    left: 290px;
    top: 62px;
    font-family: "Montserrat", sans-serif;
    color: var(--ink-soft);
  }
  .contact__name {
    font-family: "Cinzel", serif;
    font-size: 21px;
    color: var(--accent);
    letter-spacing: .06em;
    line-height: 1;
  }
  .contact__role { font-size: 10.5px; margin-top: 6px; }
  .contact__list { list-style: none; margin-top: 12px; }
  .contact__list li {
    display: flex;
    align-items: center;
    gap: 8px;
    font-size: 11.5px;
    line-height: 16px;
  }
  .contact__list svg { width: 10px; height: 10px; flex: none; }
  .contact__address { margin-top: 14px; font-size: 11.5px; line-height: 15px; }
</style>
</head>
<body>
  <section class="card card--front" aria-label="Business card front">
    <div class="brand">
      <span class="brand__dot" aria-hidden="true"></span>
      <span class="brand__name">VELMOR &amp; FIELD</span>
    </div>
    <span class="divider" aria-hidden="true"></span>
    <div class="contact">
      <p class="contact__name">Dora Plume</p>
      <p class="contact__role">CEO &amp; Founder</p>
      <ul class="contact__list">
        <li>
          <svg viewBox="0 0 10 10" aria-hidden="true"><path d="M2 1h2l1 2.5-1.3 1a5 5 0 0 0 2.8 2.8l1-1.3L10 7v2c0 .6-.4 1-1 1A9 9 0 0 1 0 1c0-.6.4-1 1-1z" fill="var(--accent)"/></svg>
          314-555-0172
        </li>
        <li>
          <svg viewBox="0 0 10 10" aria-hidden="true"><rect x="0" y="2" width="10" height="7" fill="var(--accent)"/><path d="M0 2l5 4 5-4" stroke="#fff" stroke-width="1" fill="none"/></svg>
          info@velmorandfield.com
        </li>
        <li>
          <svg viewBox="0 0 10 10" aria-hidden="true"><circle cx="5" cy="5" r="4.5" fill="var(--accent)"/><path d="M.5 5h9M5 .5c-2.4 2.6-2.4 6.4 0 9M5 .5c2.4 2.6 2.4 6.4 0 9" stroke="#fff" stroke-width=".8" fill="none"/></svg>
          www.velmorandfield.com
        </li>
      </ul>
      <p class="contact__address">Hollow Brook Farm<br>Ashgrove, MO</p>
    </div>
  </section>

  <section class="card card--back" aria-label="Business card back">
    <div class="brand">
      <span class="brand__dot" aria-hidden="true"></span>
      <span class="brand__name">VELMOR &amp; FIELD</span>
    </div>
  </section>
</body>
</html>
```